Company Collaterals

we need the different collaterals to be used for a social media company- we will be including the logo.

Industry/Entity Type

It Company

```html
<!DOCTYPE html>
<html lang="en">
<head>
<meta charset="utf-8">
<title>Kavo Social – Business Card</title>
<link rel="stylesheet" href="https://fonts.googleapis.com/css2?family=Open+Sans:ital,wght@0,400;0,600;0,700;1,700&family=Noto+Serif:wght@700&display=swap">
<style>
  :root {
    --backdrop: #a8cdf0;
    --card-blue-light: #3d8cc4;
    --card-blue-dark: #1d5f91;
    --card-white: #ffffff;
    --name-blue: #1f73b0;
    --title-green: #7aa83a;
    --brand-ink: #1b1b1b;
    --brand-dot: #2f8fd0;
    --contact-text: #ffffff;
  }
  html, body {
    margin: 0;
    width: 1200px;
    height: 825px;
    overflow: hidden;
    background: var(--backdrop);
  }
  .business-card {
    position: absolute;
    left: 110px;
    top: 132px;
    width: 980px;
    height: 560px;
    border-radius: 38px;
    overflow: hidden;
    box-shadow: 0 10px 30px rgba(20, 60, 100, 0.25);
    font-family: "Open Sans", Arial, sans-serif;
  }
  .card-surface {
    position: absolute;
    inset: 0;
    width: 100%;
    height: 100%;
  }
  .brand {
    position: absolute;
    left: 96px;
    top: 120px;
    display: flex;
    align-items: center;
    gap: 16px;
  }
  .brand-dot {
    width: 62px;
    height: 62px;
    border-radius: 50%;
    background: var(--brand-dot);
  }
  .brand-name {
    font-weight: 700;
    font-size: 54px;
    letter-spacing: 2px;
    color: var(--brand-ink);
    line-height: 1;
  }
  .holder {
    position: absolute;
    left: 72px;
    top: 300px;
  }
  .holder-name {
    font-family: "Noto Serif", Georgia, serif;
    font-weight: 700;
    font-size: 30px;
    color: var(--name-blue);
    margin: 0;
    letter-spacing: 0.5px;
  }
  .holder-title {
    font-size: 21px;
    color: var(--title-green);
    margin: 2px 0 0;
  }
  .address {
    position: absolute;
    left: 690px;
    top: 92px;
    margin: 0;
    font-size: 26px;
    line-height: 36px;
    color: var(--contact-text);
    font-style: normal;
  }
  .contact-list {
    position: absolute;
    left: 632px;
    top: 238px;
    margin: 0;
    padding: 0;
    list-style: none;
  }
  .contact-item {
    display: flex;
    align-items: center;
    gap: 14px;
    height: 50px;
    font-size: 26px;
    color: var(--contact-text);
  }
  .contact-icon {
    width: 32px;
    height: 32px;
    flex: none;
  }
  .follow {
    position: absolute;
    right: 60px;
    bottom: 70px;
    display: flex;
    align-items: center;
    gap: 12px;
    font-family: "Noto Serif", Georgia, serif;
    font-style: italic;
    font-weight: 700;
    font-size: 22px;
    color: var(--contact-text);
  }
  .social-slot {
    width: 36px;
    height: 36px;
    border-radius: 6px;
    background: var(--card-white);
  }
</style>
</head>
<body>
  <section class="business-card">
    <svg class="card-surface" viewBox="0 0 980 560" preserveAspectRatio="none" aria-hidden="true">
      <defs>
        <linearGradient id="cardBlue" x1="0" y1="1" x2="1" y2="0">
          <stop offset="0" stop-color="var(--card-blue-light)"/>
          <stop offset="1" stop-color="var(--card-blue-dark)"/>
        </linearGradient>
      </defs>
      <rect width="980" height="560" fill="url(#cardBlue)"/>
      <path d="M0,48 C110,30 190,40 250,52 C300,10 390,-10 470,20 C540,46 570,100 560,150
               C545,210 470,220 470,300 C470,390 560,440 600,560 L0,560 Z"
            fill="var(--card-white)"/>
    </svg>

    <div class="brand">
      <span class="brand-dot"></span>
      <span class="brand-name">KAVO SOCIAL</span>
    </div>

    <div class="holder">
      <p class="holder-name">MIRA CASTELL</p>
      <p class="holder-title">Managing Director</p>
    </div>

    <address class="address">PO BOX 5120,<br>HAVEN 20458, Meridia</address>

    <ul class="contact-list">
      <li class="contact-item">
        <svg class="contact-icon" viewBox="0 0 32 32" aria-hidden="true">
          <rect width="32" height="32" rx="5" fill="#fff"/>
          <path d="M10 7 l4 0 l1 5 l-3 2 c1 3 3 5 6 6 l2 -3 l5 1 l0 4 c0 1 -1 2 -2 2 c-9 0 -15 -6 -15 -15 c0 -1 1 -2 2 -2 z" fill="var(--card-blue-dark)"/>
        </svg>
        <span>55302418</span>
      </li>
      <li class="contact-item">
        <svg class="contact-icon" viewBox="0 0 32 32" aria-hidden="true">
          <rect width="32" height="32" rx="5" fill="#fff"/>
          <rect x="6" y="9" width="20" height="14" fill="none" stroke="var(--card-blue-dark)" stroke-width="2"/>
          <path d="M6 9 l10 8 l10 -8" fill="none" stroke="var(--card-blue-dark)" stroke-width="2"/>
        </svg>
        <span>mira@kavosocial.com</span>
      </li>
      <li class="contact-item">
        <svg class="contact-icon" viewBox="0 0 32 32" aria-hidden="true">
          <rect width="32" height="32" rx="5" fill="#fff"/>
          <circle cx="16" cy="16" r="9" fill="none" stroke="var(--card-blue-dark)" stroke-width="2"/>
          <ellipse cx="16" cy="16" rx="4" ry="9" fill="none" stroke="var(--card-blue-dark)" stroke-width="1.6"/>
          <path d="M7 16 h18 M9 11 h14 M9 21 h14" stroke="var(--card-blue-dark)" stroke-width="1.4"/>
        </svg>
        <span>www.kavosocial.com</span>
      </li>
    </ul>

    <div class="follow">
      <span>Follow us</span>
      <span class="social-slot"></span>
      <span class="social-slot"></span>
    </div>
  </section>
</body>
</html>
```